Restaurant service company needs a website!

I am looking for a skilled web designer/developer to create a professional, responsive, and easy-to-navigate website for my company, which specializes in servicing restaurant cooking equipment. The site should communicate trust, reliability, and technical expertise to our target audience, restaurant owners, managers, and commercial kitchen operators. I have included the company logos, if any other format for them is needed please let me know.

Target Market(s)

restaurant owners, managers, and commercial kitchen operators

Industry/Entity Type

Commercial Kitchen Equipment Service

Coding

Coded - Design and coding required

Number of Pages Required

1 page

Font styles to use
Serif
Sans Serif

Requirements
Must have
• Contact and service request forms, Click-to-call functionality for mobile, Clean, modern layout with strong visuals, Easy navigation, mobile-friendly
Nice to have
• Testimonials or Reviews, If possible a click-to-text functionality for mobile.
Should not have
• Any mention of Refrigeration or HVAC, "Free Quotes"

```html
<!DOCTYPE html>
<html lang="en">
<head>
<meta charset="UTF-8">
<title>Northgate Kitchen Services</title>
<link href="https://fonts.googleapis.com/css2?family=Oswald:wght@500;600&family=Poppins:wght@400;500&display=swap" rel="stylesheet">
<style>
:root{
  --teal:#0d6a80;
  --teal-dark:#0a5869;
  --teal-footer:#1c6f86;
  --ink:#111;
  --muted:#555;
  --grey-card:#f3f3f3;
  --white:#fff;
}
*{box-sizing:border-box;margin:0;padding:0}
html,body{width:1200px;height:3750px;overflow:hidden}
body{font-family:"Poppins",sans-serif;color:var(--ink);background:var(--white)}
.heading{font-family:"Oswald",sans-serif;font-weight:600;line-height:1.15}
section,header,footer{position:relative;width:1200px}

/* header */
.site-header{height:96px}
.topbar{position:absolute;right:0;top:0;width:900px;height:37px;background:var(--teal);clip-path:polygon(0 0,100% 0,100% 100%,30px 100%);display:flex;justify-content:flex-end;align-items:center;gap:34px;padding-right:62px;color:var(--white);font-size:14px}
.topbar span{display:flex;align-items:center;gap:9px}
.brand{position:absolute;left:60px;top:20px;display:flex;align-items:center;gap:10px}
.brand-mark{width:18px;height:18px;background:var(--teal)}
.brand-name{font-family:"Poppins",sans-serif;font-weight:500;font-size:25px;color:var(--teal);letter-spacing:1px}
.main-nav{position:absolute;right:62px;top:58px;display:flex;gap:40px;font-size:13px}
.main-nav a{color:var(--ink);text-decoration:none}
.main-nav a.active{color:var(--teal)}

/* hero */
.hero{height:660px;overflow:hidden}
.hero-photo{position:absolute;inset:0;background:linear-gradient(100deg,#15191c 0%,#2d3438 45%,#59636a 75%,#3a4146 100%)}
.hero-copy{position:absolute;left:61px;top:135px;color:var(--white)}
.hero-copy h1{font-size:47px;width:400px}
.hero-copy p{font-size:15.5px;width:360px;margin-top:22px;line-height:1.55}
.btn{display:inline-block;font-size:15px;padding:10px 16px;border-radius:4px;text-decoration:none}
.btn-teal{background:var(--teal);color:var(--white)}
.btn-white{background:var(--white);color:var(--teal)}
.hero-copy .btn{margin-top:28px}
.hero-curve{position:absolute;left:0;bottom:0}

/* about */
.about{height:489px}
.about-photo{position:absolute;left:91px;top:93px;width:471px;height:326px;border-radius:14px;background:linear-gradient(135deg,#6e5a44,#b9a184 50%,#4e5b55)}
.about-copy{position:absolute;left:638px;top:88px;width:420px}
.about-copy h2{font-size:38px}
.about-copy p{font-size:12px;color:var(--muted);line-height:1.75;margin-top:16px}
.about-copy p + p{margin-top:10px}
.about-copy .btn{margin-top:20px;padding:10px 28px}

/* services */
.services{height:510px}
.services-band{position:absolute;left:0;top:0;width:1200px;height:338px;background:var(--teal)}
.services h2{position:absolute;top:80px;width:100%;text-align:center;color:var(--white);font-size:38px}
.service-row{position:absolute;top:165px;left:171px;display:flex;gap:19px}
.service-card{width:200px;height:335px;background:var(--white);border-radius:100px 100px 60px 60px;box-shadow:0 6px 14px rgba(0,0,0,.12);position:relative;text-align:center}
.service-photo{position:absolute;left:6px;top:6px;width:188px;height:188px;border-radius:50%;background:linear-gradient(160deg,#8a8f93,#3b4650)}
.service-icon{position:absolute;left:72px;top:155px;width:56px;height:56px;border-radius:50%;background:var(--teal);border:3px solid var(--white);display:flex;align-items:center;justify-content:center}
.service-card h3{position:absolute;top:243px;width:100%;font-weight:400;font-size:15px}
.service-card .go{position:absolute;left:86px;top:285px}
.slider-arrow{position:absolute;top:310px;width:46px;height:46px;border-radius:50%;background:var(--white);box-shadow:0 2px 8px rgba(0,0,0,.2);display:flex;align-items:center;justify-content:center}

/* testimonials */
.testimonials{height:545px}
.testimonials h2{text-align:center;font-size:38px;padding-top:50px}
.testimonial-row{position:absolute;top:145px;left:174px;display:flex;gap:16px}
.testimonial{width:273px;height:345px;background:var(--grey-card);border-radius:14px;text-align:center;padding:30px 18px}
.testimonial p{font-size:12px;color:var(--muted);line-height:1.75;margin-top:16px}
.avatar{width:60px;height:60px;border-radius:50%;margin:22px auto 0;background:linear-gradient(#c9b39a,#7a6a5a)}
.testimonial .name{color:var(--teal);font-size:15px;margin-top:14px}

/* quote */
.quote{height:570px}
.quote-band{position:absolute;left:0;top:72px;width:1200px;height:498px;background:var(--teal)}
.quote-ring{position:absolute;left:880px;top:160px;width:260px;height:260px;border-radius:50%;border:30px solid rgba(255,255,255,.07)}
.quote-person{position:absolute;left:605px;top:0;width:445px;height:570px;background:linear-gradient(180deg,#3a2f29 0%,#1c1d20 40%,#101114 100%);border-radius:180px 180px 0 0}
.quote-form{position:absolute;left:60px;top:140px;color:var(--white)}
.quote-form h2{font-size:38px}
.quote-form .lead{font-size:13px;margin-top:14px;width:310px;line-height:1.55}
.field-grid{display:grid;grid-template-columns:226px 226px;gap:14px 14px;margin-top:25px}
.field{height:42px;border:1px solid rgba(255,255,255,.35);background:rgba(255,255,255,.1);border-radius:3px;font-size:12px;padding:12px 16px;color:var(--white)}
.field.full{grid-column:1/3;height:88px}
.quote-form .btn{margin-top:26px;padding:9px 27px}

/* why */
.why{height:480px}
.why h2{text-align:center;font-size:38px;padding-top:58px}
.why-row{position:absolute;top:180px;left:60px;display:flex;gap:28px}
.why-card{width:252px;height:250px;border:2px solid #cfd6d8;border-radius:6px;position:relative;padding:78px 22px 0;box-shadow:0 3px 10px rgba(0,0,0,.06)}
.why-badge{position:absolute;right:0;top:0;width:88px;height:84px;background:var(--teal);display:flex;align-items:center;justify-content:center}
.why-badge::before{content:"";position:absolute;left:-14px;top:30px;border:8px solid transparent;border-right-color:var(--teal);border-left-width:6px}
.why-card .num{font-weight:500;font-size:18px}
.why-card h3{font-weight:500;font-size:19px;color:#444;margin-top:12px;line-height:1.25}
.why-card p{font-size:12px;color:var(--muted);line-height:1.75;margin-top:12px}

/* footer */
.site-footer{height:400px;background:var(--teal-footer);color:var(--white)}
.footer-brand{position:absolute;top:55px;width:100%;display:flex;justify-content:center;align-items:center;gap:10px}
.footer-brand .brand-mark{background:var(--white)}
.footer-brand .brand-name{color:var(--white)}
.footer-col{position:absolute;top:148px}
.footer-col h4{font-family:"Oswald",sans-serif;font-weight:500;font-size:22px}
.footer-col ul{list-style:none;margin-top:12px;font-size:13px;line-height:22.5px}
.col-divider{position:absolute;top:150px;width:1px;height:170px;background:rgba(255,255,255,.25)}
.contact-line{display:flex;align-items:center;gap:18px;margin-top:14px;font-size:13px;line-height:1.5}
.contact-dot{width:32px;height:32px;border-radius:50%;background:var(--white);display:flex;align-items:center;justify-content:center;flex:none}
.footer-bottom{position:absolute;left:60px;right:60px;bottom:0;height:44px;border-top:1px solid rgba(255,255,255,.25);text-align:center;font-size:12px;padding-top:14px}
</style>
</head>
<body>

<header class="site-header">
  <div class="topbar">
    <span><svg width="16" height="16" viewBox="0 0 24 24" fill="#fff"><path d="M6.6 10.8a15 15 0 0 0 6.6 6.6l2.2-2.2c.3-.3.7-.4 1-.2 1.1.4 2.3.6 3.6.6.6 0 1 .4 1 1V20c0 .6-.4 1-1 1A17 17 0 0 1 3 4c0-.6.4-1 1-1h3.5c.6 0 1 .4 1 1 0 1.3.2 2.5.6 3.6.1.3 0 .7-.2 1z"/></svg>+1 555 014 2290</span>
    <span><svg width="17" height="14" viewBox="0 0 24 18" fill="#fff"><path d="M2 0h20a2 2 0 0 1 2 2v14a2 2 0 0 1-2 2H2a2 2 0 0 1-2-2V2a2 2 0 0 1 2-2zm0 3v1l10 6 10-6V3L12 9z"/></svg>hello@northgateservice.com</span>
  </div>
  <div class="brand"><span class="brand-mark"></span><span class="brand-name">NORTHGATE</span></div>
  <nav class="main-nav">
    <a class="active" href="#">Home</a><a href="#">About Us</a><a href="#">Our Services</a><a href="#">Why Chooes us</a><a href="#">Testimonial</a><a href="#">Contact</a>
  </nav>
</header>

<section class="hero">
  <div class="hero-photo" role="img" aria-label="Commercial kitchen with stainless steel ranges, pots and hanging utensils"></div>
  <div class="hero-copy">
    <h1 class="heading">Reliable Service for Your Commercial Kitchen Equipment</h1>
    <p>Keeping restaurants running smoothly with trusted repair and maintenance solutions.</p>
    <a class="btn btn-teal" href="#">BOOK A SERVICES</a>
  </div>
  <svg class="hero-curve" width="1200" height="100" viewBox="0 0 1200 100">
    <path d="M0 20 Q600 150 1200 20 L1200 100 L0 100 Z" fill="#fff"/>
    <path d="M0 20 Q600 150 1200 20" fill="none" stroke="#0d6a80" stroke-width="3"/>
  </svg>
</section>

<section class="about">
  <div class="about-photo" role="img" aria-label="Two smiling restaurant staff in aprons standing behind a bar"></div>
  <div class="about-copy">
    <h2 class="heading">About Northgate<br>Restaurant Services</h2>
    <p>Lorem Ipsum has been the industry's standard dummy text ever since the 1500s, when an unknown printer took a galley of type and scrambled it to make a type specimen book. It has survived not only five centuries, but also the leap into electronic typesetting, remaining essentially unchanged.</p>
    <p>Lorem Ipsum has been the industry's standard dummy text ever since the 1500s, when an unknown printer took a galley of type and scrambled it to make a type specimen book.</p>
    <a class="btn btn-teal" href="#">Read More</a>
  </div>
</section>

<section class="services">
  <div class="services-band"></div>
  <h2 class="heading">Our Services</h2>
  <div class="slider-arrow" style="left:60px"><svg width="18" height="18" viewBox="0 0 24 24" fill="none" stroke="#111" stroke-width="2"><path d="M20 12H4M10 6l-6 6 6 6"/></svg></div>
  <div class="slider-arrow" style="left:1092px"><svg width="18" height="18" viewBox="0 0 24 24" fill="none" stroke="#111" stroke-width="2"><path d="M4 12h16M14 6l6 6-6 6"/></svg></div>
  <div class="service-row">
    <article class="service-card">
      <div class="service-photo" role="img" aria-label="Technician repairing a commercial oven"></div>
      <div class="service-icon"><svg width="28" height="28" viewBox="0 0 24 24" fill="none" stroke="#fff" stroke-width="1.6"><rect x="3" y="7" width="18" height="13" rx="1"/><path d="M3 11h18M8 4h8v3"/></svg></div>
      <h3>Equipment Repair</h3>
      <svg class="go" width="28" height="28" viewBox="0 0 28 28" fill="none" stroke="#111" stroke-width="1.4"><circle cx="14" cy="14" r="13"/><path d="M12 9l5 5-5 5"/></svg>
    </article>
    <article class="service-card">
      <div class="service-photo" role="img" aria-label="Technician servicing a kitchen fryer"></div>
      <div class="service-icon"><svg width="28" height="28" viewBox="0 0 24 24" fill="none" stroke="#fff" stroke-width="1.6"><circle cx="12" cy="10" r="4"/><path d="M12 3v2M12 15v2M5 10h2M17 10h2M5 21h14"/></svg></div>
      <h3>Preventive Maintenance</h3>
      <svg class="go" width="28" height="28" viewBox="0 0 28 28" fill="none" stroke="#111" stroke-width="1.4"><circle cx="14" cy="14" r="13"/><path d="M12 9l5 5-5 5"/></svg>
    </article>
    <article class="service-card">
      <div class="service-photo" role="img" aria-label="Engineer working on a kitchen unit"></div>
      <div class="service-icon"><svg width="30" height="30" viewBox="0 0 24 24" fill="none" stroke="#fff" stroke-width="1.4"><circle cx="12" cy="12" r="9"/><text x="12" y="15" font-size="8" text-anchor="middle" fill="#fff" stroke="none" font-family="Poppins,sans-serif">24</text></svg></div>
      <h3>Emergency Service</h3>
      <svg class="go" width="28" height="28" viewBox="0 0 28 28" fill="none" stroke="#111" stroke-width="1.4"><circle cx="14" cy="14" r="13"/><path d="M12 9l5 5-5 5"/></svg>
    </article>
    <article class="service-card">
      <div class="service-photo" role="img" aria-label="Chefs in a busy commercial kitchen"></div>
      <div class="service-icon"><svg width="28" height="28" viewBox="0 0 24 24" fill="none" stroke="#fff" stroke-width="1.6"><rect x="4" y="4" width="16" height="16" rx="1"/><circle cx="15" cy="15" r="3"/><path d="M7 8h6"/></svg></div>
      <h3>Installation Support</h3>
      <svg class="go" width="28" height="28" viewBox="0 0 28 28" fill="none" stroke="#111" stroke-width="1.4"><circle cx="14" cy="14" r="13"/><path d="M12 9l5 5-5 5"/></svg>
    </article>
  </div>
</section>

<section class="testimonials">
  <h2 class="heading">Client Testimonials</h2>
  <div class="testimonial-row">
    <article class="testimonial">
      <svg width="36" height="28" viewBox="0 0 36 28" fill="#0d6a80"><path d="M0 28V14C0 6 4 1 12 0l1 4c-4 1-6 4-6 8h6v16zM21 28V14c0-8 4-13 12-14l1 4c-4 1-6 4-6 8h6v16z"/></svg>
      <p>Lorem Ipsum has been the industry's standard dummy text ever since the 1500s, when an unknown printer took a galley of type and scrambled it to make a type specimen book. It has survived not only five centuries...</p>
      <div class="avatar" role="img" aria-label="Client portrait"></div>
      <div class="name">Client Name</div>
    </article>
    <article class="testimonial">
      <svg width="36" height="28" viewBox="0 0 36 28" fill="#0d6a80"><path d="M0 28V14C0 6 4 1 12 0l1 4c-4 1-6 4-6 8h6v16zM21 28V14c0-8 4-13 12-14l1 4c-4 1-6 4-6 8h6v16z"/></svg>
      <p>Lorem Ipsum has been the industry's standard dummy text ever since the 1500s, when an unknown printer took a galley of type and scrambled it to make a type specimen book. It has survived not only five centuries...</p>
      <div class="avatar" role="img" aria-label="Client portrait"></div>
      <div class="name">Client Name</div>
    </article>
    <article class="testimonial">
      <svg width="36" height="28" viewBox="0 0 36 28" fill="#0d6a80"><path d="M0 28V14C0 6 4 1 12 0l1 4c-4 1-6 4-6 8h6v16zM21 28V14c0-8 4-13 12-14l1 4c-4 1-6 4-6 8h6v16z"/></svg>
      <p>Lorem Ipsum has been the industry's standard dummy text ever since the 1500s, when an unknown printer took a galley of type and scrambled it to make a type specimen book. It has survived not only five centuries...</p>
      <div class="avatar" role="img" aria-label="Client portrait"></div>
      <div class="name">Client Name</div>
    </article>
  </div>
</section>

<section class="quote">
  <div class="quote-band"></div>
  <div class="quote-ring"></div>
  <div class="quote-person" role="img" aria-label="Bearded man in a dark suit and striped tie"></div>
  <form class="quote-form">
    <h2 class="heading">Get A Quote</h2>
    <p class="lead">Fill in the form below to receive a callback from one of our team.</p>
    <div class="field-grid">
      <div class="field">First Name *</div>
      <div class="field">Last Name *</div>
      <div class="field">Email *</div>
      <div class="field">Phone Number *</div>
      <div class="field full">Message *</div>
    </div>
    <a class="btn btn-white" href="#">Read More</a>
  </form>
</section>

<section class="why">
  <h2 class="heading">Why Chooes Us</h2>
  <div class="why-row">
    <article class="why-card">
      <div class="why-badge"><svg width="40" height="40" viewBox="0 0 24 24" fill="none" stroke="#fff" stroke-width="1.2"><circle cx="12" cy="7" r="4"/><path d="M4 21c0-4 4-7 8-7s8 3 8 7"/></svg></div>
      <div class="num">01.</div><h3>Certified<br>Technicians</h3>
      <p>Lorem Ipsum has been the industry's standard dummy text ever since the 1500s.</p>
    </article>
    <article class="why-card">
      <div class="why-badge"><svg width="40" height="40" viewBox="0 0 24 24" fill="none" stroke="#fff" stroke-width="1.2"><circle cx="13" cy="13" r="7"/><path d="M13 9v4l3 2M2 10h4M3 14h3"/></svg></div>
      <div class="num">02.</div><h3>Fast Response<br>Times</h3>
      <p>Lorem Ipsum has been the industry's standard dummy text ever since the 1500s.</p>
    </article>
    <article class="why-card">
      <div class="why-badge"><svg width="40" height="40" viewBox="0 0 24 24" fill="none" stroke="#fff" stroke-width="1.2"><path d="M4 17a8 8 0 0 1 16 0zM2 19h20M12 6v3"/></svg></div>
      <div class="num">03.</div><h3>Trusted by<br>Restaurants</h3>
      <p>Lorem Ipsum has been the industry's standard dummy text ever since the 1500s.</p>
    </article>
    <article class="why-card">
      <div class="why-badge"><svg width="40" height="40" viewBox="0 0 24 24" fill="none" stroke="#fff" stroke-width="1.2"><circle cx="12" cy="12" r="9"/><text x="12" y="15" font-size="7" text-anchor="middle" fill="#fff" stroke="none" font-family="Poppins,sans-serif">24</text></svg></div>
      <div class="num">04.</div><h3>24/7 Emergency<br>Support</h3>
      <p>Lorem Ipsum has been the industry's standard dummy text ever since the 1500s.</p>
    </article>
  </div>
</section>

<footer class="site-footer">
  <div class="footer-brand"><span class="brand-mark"></span><span class="brand-name">NORTHGATE</span></div>
  <div class="footer-col" style="left:61px">
    <h4>Navigation</h4>
    <ul><li>Home</li><li>About Us</li><li>Services</li><li>Why Chooes Us</li><li>Testimonial</li><li>Contact US</li></ul>
  </div>
  <div class="col-divider" style="left:417px"></div>
  <div class="footer-col" style="left:441px">
    <h4>Our Services</h4>
    <ul><li>Equipment Repair</li><li>Preventive Maintenance</li><li>Emergency Service</li><li>Installation Support</li></ul>
  </div>
  <div class="col-divider" style="left:781px"></div>
  <div class="footer-col" style="left:805px">
    <h4>Contact Now</h4>
    <div class="contact-line"><span class="contact-dot"><svg width="15" height="15" viewBox="0 0 24 24" fill="#1c6f86"><path d="M6.6 10.8a15 15 0 0 0 6.6 6.6l2.2-2.2c.3-.3.7-.4 1-.2 1.1.4 2.3.6 3.6.6.6 0 1 .4 1 1V20c0 .6-.4 1-1 1A17 17 0 0 1 3 4c0-.6.4-1 1-1h3.5c.6 0 1 .4 1 1 0 1.3.2 2.5.6 3.6.1.3 0 .7-.2 1z"/></svg></span>+1 555 014 2290</div>
    <div class="contact-line"><span class="contact-dot"><svg width="15" height="12" viewBox="0 0 24 18" fill="#1c6f86"><path d="M2 0h20a2 2 0 0 1 2 2v14a2 2 0 0 1-2 2H2a2 2 0 0 1-2-2V2a2 2 0 0 1 2-2zm0 3v1l10 6 10-6V3L12 9z"/></svg></span>hello@northgateservice.com</div>
    <div class="contact-line"><span class="contact-dot"><svg width="13" height="16" viewBox="0 0 24 30" fill="#1c6f86"><path d="M12 0a12 12 0 0 1 12 12c0 9-12 18-12 18S0 21 0 12A12 12 0 0 1 12 0zm0 7a5 5 0 1 0 0 10 5 5 0 0 0 0-10z"/></svg></span>Lorem Ipsum has been the<br>industry's standard</div>
  </div>
  <div class="footer-bottom">Copyright © 2025 Northgate Restaurant Services. All Rights Reserved.</div>
</footer>

</body>
</html>
```